Need (3) Christmas Calendar Designs for the United States Market (English)

I need (3) Christmas calendars designed for me. Sample file below so you can see the layout. Need to keep the blank spaces open for pics to be dropped in later, but otherwise create some nice Holiday/Christmas centric themed calendars for this project. You can change the date format anyway that you want and add background images to the date section of the calendar, but the top needs to remain fairly blank for pictures

Target Market(s)

everyday consumer that wants a Holiday/Christmas calendar. We will be adding customers pictures later on.

Font styles to use
Decorative

Requirements
Must have
• Follow format and size of sample file and have a Holiday theme, snowflakes, christmas trees, santa claus etc, etc. Must be in a 2016 calendar year
Nice to have
• This is a pretty basic project, when you look at the sample file that I provided. Would just like it to be festive with some pretty, vibrant colors, but the dates must still be easy to see. Maybe add a notes section to
Should not have
• any dates/format other then 2016 calendar year

```html
<!DOCTYPE html>
<html lang="en">
<head>
<meta charset="utf-8">
<title>Images of You 2016 – Holiday Calendar</title>
<link href="https://fonts.googleapis.com/css2?family=Fredericka+the+Great&family=Open+Sans:wght@300;400&display=swap" rel="stylesheet">
<style>
  :root {
    --ink-green: #1f5a32;
    --cocoa: #7a5a3e;
    --cream: #f6e6c4;
    --paper: #ffffff;
    --grid-line: #2a2a2a;
    --date-grey: #e2e2e2;
    --deer-brown: #4a1f17;
    --deer-green: #1f6b3a;
  }
  html, body {
    margin: 0;
    padding: 0;
    width: 1200px;
    height: 1000px;
    overflow: hidden;
    background: #ffffff;
  }
  .canvas {
    position: relative;
    width: 1200px;
    height: 1000px;
  }

  /* ---------- Month page ---------- */
  .month-page {
    position: absolute;
    left: 30px;
    top: 25px;
    width: 600px;
    height: 950px;
    background: var(--paper);
    box-shadow: 0 0 0 1px #dddddd, 2px 4px 10px rgba(0,0,0,.18);
  }
  .month-page__photo-area {
    position: relative;
    height: 440px;
    background: linear-gradient(to bottom, #86654a 0%, #b99d80 12%, #efe5d8 30%, #fbf8f3 50%, #ffffff 70%);
    border-bottom: 1px solid #cfcfcf;
  }
  .month-page__title {
    position: absolute;
    left: 34px;
    top: 100px;
    margin: 0;
    font-family: "Fredericka the Great", cursive;
    font-weight: 400;
    font-size: 40px;
    font-variant: small-caps;
    color: var(--ink-green);
    letter-spacing: 1px;
  }
  .reindeer {
    position: absolute;
    background: linear-gradient(160deg, #8c5a4a 0%, var(--deer-brown) 60%, var(--deer-green) 100%);
    opacity: .85;
    border-radius: 6px;
  }
  .month-page__reindeer { left: 65px; top: 270px; width: 160px; height: 160px; }

  .month-grid {
    position: absolute;
    left: 30px;
    top: 470px;
    width: 540px;
    border-collapse: collapse;
    table-layout: fixed;
    font-family: "Open Sans", sans-serif;
  }
  .month-grid th {
    height: 16px;
    font-size: 9px;
    font-weight: 400;
    color: #333333;
    border: 1px solid var(--grid-line);
    padding: 0;
  }
  .month-grid td {
    position: relative;
    height: 72px;
    border: 1px solid var(--grid-line);
    padding: 0;
    vertical-align: bottom;
  }
  .month-grid .date {
    display: block;
    padding: 0 0 0 8px;
    font-size: 46px;
    font-weight: 300;
    line-height: 1;
    color: var(--date-grey);
    letter-spacing: -2px;
  }
  .month-grid__reindeer { left: 8px; bottom: 4px; width: 56px; height: 62px; }

  /* ---------- Cover page ---------- */
  .cover-page {
    position: absolute;
    left: 660px;
    top: 150px;
    width: 515px;
    height: 530px;
    background: radial-gradient(ellipse at 45% 45%, #fbf1da 0%, var(--cream) 35%, #c9ab86 80%, #8d6b4e 100%);
    box-shadow: 2px 4px 10px rgba(0,0,0,.18);
  }
  .cover-page__title {
    margin: 0;
    padding-top: 28px;
    text-align: center;
    font-family: "Fredericka the Great", cursive;
    font-weight: 400;
    color: var(--ink-green);
    line-height: 1.05;
  }
  .cover-page__headline {
    display: block;
    font-size: 64px;
    font-variant: small-caps;
  }
  .cover-page__year {
    display: block;
    font-size: 44px;
  }
  .cover-page__reindeer { right: 24px; bottom: 20px; width: 140px; height: 180px; }
</style>
</head>
<body>
<main class="canvas">

  <section class="month-page" aria-label="January 2016 calendar page">
    <header class="month-page__photo-area">
      <h1 class="month-page__title">January 2016</h1>
      <div class="reindeer month-page__reindeer" role="img" aria-label="Illustration of a swirly-antlered reindeer wearing a green scarf and boots"></div>
    </header>

    <table class="month-grid">
      <thead>
        <tr><th>Sunday</th><th>Monday</th><th>Tuesday</th><th>Wednesday</th><th>Thursday</th><th>Friday</th><th>Saturday</th></tr>
      </thead>
      <tbody>
        <tr><td></td><td></td><td></td><td></td><td><span class="date">1</span></td><td><span class="date">2</span></td><td><span class="date">3</span></td></tr>
        <tr><td><span class="date">4</span></td><td><span class="date">5</span></td><td><span class="date">6</span></td><td><span class="date">7</span></td><td><span class="date">8</span></td><td><span class="date">9</span></td><td><span class="date">10</span></td></tr>
        <tr><td><span class="date">11</span></td><td><span class="date">12</span></td><td><span class="date">13</span></td><td><span class="date">14</span></td><td><span class="date">15</span></td><td><span class="date">16</span></td><td><span class="date">17</span></td></tr>
        <tr><td><span class="date">18</span></td><td><span class="date">19</span></td><td><span class="date">20</span></td><td><span class="date">21</span></td><td><span class="date">22</span></td><td><span class="date">23</span></td><td><span class="date">24</span></td></tr>
        <tr><td><span class="date">25</span></td><td><span class="date">26</span></td><td><span class="date">27</span></td><td><span class="date">28</span></td><td><span class="date">29</span></td><td><span class="date">30</span></td><td><span class="date">31</span></td></tr>
        <tr><td><div class="reindeer month-grid__reindeer" role="img" aria-label="Small reindeer illustration with green scarf"></div></td><td></td><td></td><td></td><td></td><td></td><td></td></tr>
      </tbody>
    </table>
  </section>

  <section class="cover-page" aria-label="Calendar cover">
    <h2 class="cover-page__title">
      <span class="cover-page__headline">Images of you</span>
      <span class="cover-page__year">2016</span>
    </h2>
    <div class="reindeer cover-page__reindeer" role="img" aria-label="Illustration of a swirly-antlered reindeer with green scarf among snowflakes"></div>
  </section>

</main>
</body>
</html>
```